Law Firm Website, easily updated by User

We are a regional Labor and Employment Law Firm with a tired outdated website. We are looking for a clean easy to use website that will allow us to easily update information and articles in house. Our current website can be found at www.quillbrookcounsel.com

Industry/Entity Type

Labor

Number of Pages Required

5+ page

Colors
0655a3

Requirements
Must have
• Content easily updated by user
Nice to have
• crisp clean pages
Should not have
• stock pictures

```html
<!DOCTYPE html>
<html lang="en">
<head>
<meta charset="utf-8">
<title>Quillbrook &amp; Partners, P.C. — Employment Counseling, Litigation, Labor &amp; Benefits Law</title>
<link rel="stylesheet" href="https://fonts.googleapis.com/css2?family=Tinos:ital,wght@0,400;0,700;1,400&display=swap">
<style>
  :root {
    --brand-blue: #243f8f;
    --band-blue: #1c4a8a;
    --nav-dark: #3d3d3d;
    --nav-text: #a9a9a9;
    --hero-top: #8a8787;
    --hero-bottom: #3b3b3b;
    --text-grey: #9a9a9a;
    --box-border: #8c8c8c;
    --footer-black: #050505;
    --white: #ffffff;
  }
  * { box-sizing: border-box; margin: 0; padding: 0; }
  html, body { width: 796px; height: 1200px; overflow: hidden; background: var(--white); }
  body { position: relative; font-family: "Tinos", "Times New Roman", serif; }

  /* Navigation */
  .site-nav {
    position: absolute; top: 0; left: 109px; width: 594px; height: 40px;
    background: var(--nav-dark); display: flex; align-items: stretch;
    justify-content: space-between; padding-right: 16px;
  }
  .site-nav a {
    color: var(--nav-text); text-decoration: none; font-size: 20px;
    padding: 0 8px; display: flex; align-items: center; white-space: nowrap;
  }
  .site-nav a.is-current { background: var(--white); color: var(--brand-blue); padding: 0 5px; }

  /* Brand */
  .brand {
    position: absolute; top: 50px; left: 0; width: 796px; height: 56px;
    display: flex; justify-content: center; align-items: center; gap: 10px;
  }
  .brand-mark { width: 22px; height: 22px; background: var(--brand-blue); }
  .brand-name { font-size: 26px; color: var(--brand-blue); }

  /* Hero */
  .hero {
    position: absolute; top: 116px; left: 0; width: 796px; height: 377px;
    background: linear-gradient(180deg, var(--hero-top), var(--hero-bottom));
  }
  .hero-photo {
    position: absolute; top: 12px; left: 97px; width: 603px; height: 320px;
    background: radial-gradient(ellipse at 55% 40%, #e6e6e6 0%, #b9b9b9 55%, #6f6f6f 100%);
  }
  .hero-caption {
    position: absolute; top: 332px; left: 97px; width: 603px; height: 31px;
    background: var(--white); color: var(--brand-blue); font-size: 17.5px;
    display: flex; align-items: center; justify-content: center; white-space: nowrap;
  }

  /* Practice areas */
  .practice-grid {
    position: absolute; top: 503px; left: 97px; width: 603px;
    display: grid; grid-template-columns: repeat(3, 171px); column-gap: 45px; row-gap: 5px;
  }
  .practice-card {
    height: 122px; border: 1px solid var(--box-border); padding: 4px 9px;
  }
  .practice-card h3 {
    color: var(--brand-blue); font-size: 20px; line-height: 21px; font-weight: 700;
    height: 44px; white-space: nowrap;
  }
  .practice-card p { color: var(--text-grey); font-size: 14.5px; line-height: 21px; margin-top: 2px; }

  /* Info band */
  .info-band {
    position: absolute; top: 893px; left: 0; width: 796px; height: 223px;
    background: var(--band-blue); color: var(--white);
  }
  .welcome { position: absolute; left: 99px; top: 7px; width: 320px; }
  .band-heading {
    font-size: 20px; font-weight: 700; padding-bottom: 5px;
    border-bottom: 1px solid var(--white);
  }
  .welcome .band-heading { width: 169px; }
  .welcome p { font-size: 15.5px; line-height: 20.5px; margin-top: 14px; padding-left: 3px; }

  .latest-news { position: absolute; left: 533px; top: 7px; width: 167px; }
  .latest-news .band-heading { width: 167px; }
  .news-item {
    display: flex; gap: 10px; margin-left: -10px; width: 177px;
    padding: 10px 0 8px; border-bottom: 1px dotted rgba(255,255,255,0.7);
  }
  .news-item:last-of-type { border-bottom: none; }
  .news-date {
    flex: 0 0 48px; height: 30px; margin-top: 17px; background: #3a3a3a;
    border: 1px solid #c8c8c8; font-size: 9px; font-weight: 700; text-align: center; line-height: 12px; padding-top: 2px;
  }
  .news-date span { display: block; font-size: 10px; }
  .news-body h4 { font-size: 11px; font-weight: 700; margin-bottom: 5px; }
  .news-body p { font-size: 9px; line-height: 10.5px; text-transform: uppercase; }
  .read-more {
    position: absolute; left: 55px; top: 198px; font-size: 13px; font-weight: 700;
    display: flex; align-items: center; gap: 6px; color: var(--white); text-decoration: none;
  }

  /* Footer */
  .site-footer {
    position: absolute; top: 1116px; left: 0; width: 796px; height: 84px;
    background: var(--footer-black); color: var(--white);
  }
  .legal { position: absolute; left: 99px; top: 19px; font-size: 9px; font-weight: 700; line-height: 24px; }
  .consult { position: absolute; left: 478px; top: 11px; width: 230px; text-align: center; font-weight: 700; }
  .consult .lead { font-size: 17px; }
  .consult .phone { font-size: 27px; margin-top: 3px; white-space: nowrap; }
</style>
</head>
<body>
  <nav class="site-nav">
    <a href="#" class="is-current">Home</a>
    <a href="#">Attorneys</a>
    <a href="#">Practice Areas</a>
    <a href="#">News</a>
    <a href="#">Employers</a>
    <a href="#">Contact</a>
  </nav>

  <header class="brand">
    <span class="brand-mark"></span>
    <span class="brand-name">Quillbrook &amp; Partners, P.C.</span>
  </header>

  <section class="hero">
    <div class="hero-photo" role="img" aria-label="Photograph of the firm's three attorneys in business suits"></div>
    <p class="hero-caption">Counseling and Advising Clients Exclusively on Laws of the Workplace</p>
  </section>

  <section class="practice-grid">
    <article class="practice-card"><h3>Employment<br>Law</h3><p>Lorem Ipsum is simply dummy text of the printing and typesetting</p></article>
    <article class="practice-card"><h3>ERISA<br>Law</h3><p>Lorem Ipsum is simply dummy text of the printing and typesetting</p></article>
    <article class="practice-card"><h3>Civil<br>Litigation</h3><p>Lorem Ipsum is simply dummy text of the printing and typesetting</p></article>
    <article class="practice-card"><h3>Railway<br>Labor Act</h3><p>Lorem Ipsum is simply dummy text of the printing and typesetting</p></article>
    <article class="practice-card"><h3>Hotel<br>Law</h3><p>Lorem Ipsum is simply dummy text of the printing and typesetting</p></article>
    <article class="practice-card"><h3>Non-Profit<br>Law</h3><p>Lorem Ipsum is simply dummy text of the printing and typesetting</p></article>
    <article class="practice-card"><h3>Federal False<br>Claims Act</h3><p>Lorem Ipsum is simply dummy text of the printing and typesetting</p></article>
    <article class="practice-card"><h3>Human<br>Resources</h3><p>Lorem Ipsum is simply dummy text of the printing and typesetting</p></article>
    <article class="practice-card"><h3>Lectures and<br>Training</h3><p>Lorem Ipsum is simply dummy text of the printing and typesetting</p></article>
  </section>

  <section class="info-band">
    <div class="welcome">
      <h2 class="band-heading">Welcome</h2>
      <p>Lorem Ipsum is simply dummy text of the printing and typesetting industry. Lorem Ipsum has been the industry's standard dummy text ever since the 1500s, when an unknown printer took a galley of type and scrambled it to make a type specimen book. It has survived not only five centuries, but also the leap into electronic typesetting, remaining essentially</p>
    </div>
    <div class="latest-news">
      <h2 class="band-heading">Latest News</h2>
      <div class="news-item">
        <div class="news-date">19 MAY<span>2014</span></div>
        <div class="news-body"><h4>LOREM IPSUM</h4><p>Is simply dummy text of the printing and typesetting industry. Lorem ipsum has</p></div>
      </div>
      <div class="news-item">
        <div class="news-date">19 MAY<span>2014</span></div>
        <div class="news-body"><h4>LOREM IPSUM</h4><p>Is simply dummy text of the printing and typesetting industry. Lorem ipsum has</p></div>
      </div>
      <a class="read-more" href="#">READ MORE
        <svg width="16" height="11" viewBox="0 0 16 11" aria-hidden="true"><path d="M1 1l4.5 4.5L1 10M8 1l4.5 4.5L8 10" fill="none" stroke="#fff" stroke-width="2.4"/></svg>
      </a>
    </div>
  </section>

  <footer class="site-footer">
    <div class="legal">
      <p>Copyright © 2013. All Rights Reserved. Quillbrook &amp; Partners, P.C.</p>
      <p>Privacy Policy | Disclaimer</p>
    </div>
    <div class="consult">
      <p class="lead">For a Free Consultation</p>
      <p class="phone">Call (555) 014-2837</p>
    </div>
  </footer>
</body>
</html>
```